Vemtra Group: Business Card for a high end technology company

We need a cool new design for our business cards using our cloud logo. We are a technology consulting business. We pride ourselves on be the best of the best. We mainly focus on cloud solutions and managed services. We need a business card that sets us apart from the other technology companies in the area and allows us to stand out.

Target Market(s)

Technology departments, CIO, CEOs, and Information Technology Staff.

Industry/Entity Type

Information Technology

Contact Information for Business Card

Must have the logo and our name.
Must have employee name, email address, office phone, cell phone and website.
Need to have all info on one side a cool design on backside.

Font styles to use
Serif
Sans Serif

Requirements
Must have
• Must have the logo and our name.
• Must have employee name, email address, office phone, cell phone and website.
• Need to have all info on one side a cool design on back side.
• Must be a crisp clean design, not too busy or confusing.

```html
<!DOCTYPE html>
<html lang="en">
<head>
<meta charset="utf-8">
<title>Vemtra Group – Business Card</title>
<link rel="stylesheet" href="https://fonts.googleapis.com/css2?family=Montserrat:wght@300;400;500&display=swap">
<style>
  :root {
    --bg: #e9eaec;
    --card-white: #ffffff;
    --brand-blue: #3aaee4;
    --ink-dark: #3a3a3c;
    --band-dark: #39393b;
    --swoosh-grey: #5a5a5c;
    --text-light: #ffffff;
  }
  * { box-sizing: border-box; margin: 0; padding: 0; }
  html, body { width: 1200px; height: 900px; overflow: hidden; }
  body {
    background: var(--bg);
    font-family: "Montserrat", sans-serif;
    position: relative;
  }
  .card {
    position: absolute;
    top: 140px;
    width: 360px;
    height: 620px;
    border-radius: 24px;
    overflow: hidden;
    background: var(--card-white);
    box-shadow: 0 10px 30px rgba(0,0,0,0.18);
  }
  .card--front { left: 200px; }
  .card--back { left: 640px; }

  .card__art { position: absolute; inset: 0; }

  .brand {
    position: absolute;
    left: 0; right: 0;
    display: flex;
    align-items: center;
    justify-content: center;
    gap: 12px;
  }
  .brand__dot {
    width: 34px; height: 34px;
    border-radius: 50%;
    background: var(--brand-blue);
  }
  .brand__name {
    font-weight: 400;
    font-size: 34px;
    color: var(--ink-dark);
    letter-spacing: 0.5px;
  }
  .card--front .brand { top: 110px; }

  .contact {
    position: absolute;
    top: 260px;
    left: 0; right: 0;
    text-align: center;
    color: var(--text-light);
  }
  .contact__name {
    font-size: 23px;
    font-weight: 400;
    letter-spacing: 0.5px;
  }
  .contact__title {
    font-size: 14px;
    font-weight: 300;
    margin-top: 4px;
  }
  .contact__rule {
    width: 230px;
    height: 1px;
    margin: 16px auto 20px;
    background: rgba(255,255,255,0.7);
  }
  .contact__address, .contact__lines {
    font-size: 15px;
    font-weight: 400;
    line-height: 1.55;
  }
  .contact__lines { margin-top: 28px; }

  .web {
    position: absolute;
    bottom: 32px;
    left: 0; right: 0;
    text-align: center;
    color: var(--text-light);
    font-size: 19px;
    font-weight: 500;
    letter-spacing: 0.5px;
  }
  .web__domain { color: var(--brand-blue); }

  .card--back .brand { top: 250px; }
  .back__web {
    position: absolute;
    top: 302px;
    left: 0; right: 0;
    text-align: center;
    font-size: 11px;
    font-weight: 500;
    color: var(--ink-dark);
  }
  .back__strip {
    position: absolute;
    left: 0; right: 0; bottom: 0;
    height: 14px;
    background: var(--brand-blue);
  }
</style>
</head>
<body>

  <section class="card card--front">
    <svg class="card__art" width="360" height="620" viewBox="0 0 360 620" aria-hidden="true">
      <path d="M0 520 L0 250 Q180 160 360 250 L360 520 Z" fill="var(--brand-blue)"/>
      <path d="M0 232 Q180 142 360 232 L360 246 Q180 156 0 246 Z" fill="var(--swoosh-grey)"/>
      <path d="M166 196 L194 196 L180 210 Z" fill="var(--swoosh-grey)"/>
      <path d="M0 500 Q0 528 28 528 L332 528 Q360 528 360 500 L360 620 L0 620 Z" fill="var(--band-dark)"/>
    </svg>

    <div class="brand">
      <span class="brand__dot"></span>
      <span class="brand__name">Vemtra Group</span>
    </div>

    <div class="contact">
      <p class="contact__name">YOUR NAME</p>
      <p class="contact__title">Title</p>
      <div class="contact__rule"></div>
      <p class="contact__address">1475 North Cedar Ridge Ave<br>Suite 210-318 Lakemont, AZ</p>
      <p class="contact__lines">O : 0455120874<br>M : 0455120874<br>info@vemtragroup.com</p>
    </div>

    <p class="web">www.<span class="web__domain">vemtragroup</span>.com</p>
  </section>

  <section class="card card--back">
    <div class="brand">
      <span class="brand__dot"></span>
      <span class="brand__name">Vemtra Group</span>
    </div>
    <p class="back__web">www.vemtragroup.com</p>
    <div class="back__strip"></div>
  </section>

</body>
</html>
```